AUSTRALIAN CONSULTING FIRM BUSINESS CARD - MODERN

We are wanting a modern, clean lined business card design. We are professional niche consultancy firm situated in Australia called Marlow Advisory Partners Pty Ltd.
The card should communicate professionalism and creativity and draw on our logo design (attached).
The design should be two sided, landscape orientation.
Target Market(s)
government, not for profit sector, corporate clients
Industry/Entity Type
Landscape
Requirements
Must have
- logo
no new introduced colours

```html
<!DOCTYPE html>
<html lang="en">
<head>
<meta charset="utf-8">
<title>Marlow Advisory Partners – Business Card</title>
<link href="https://fonts.googleapis.com/css2?family=PT+Sans:wght@400;700&display=swap" rel="stylesheet">
<style>
  :root {
    --page: #ffffff;
    --ink: #1a1a1a;
    --brand-navy: #1f4fa0;
    --brand-blue: #1aa3e0;
    --brand-purple: #a64ca6;
    --brand-green: #7dc142;
    --green-deep: #6fb83a;
    --green-glow: #f4f9ee;
  }
  * { box-sizing: border-box; margin: 0; padding: 0; }
  html, body { width: 1200px; height: 900px; overflow: hidden; background: var(--page); }
  body { font-family: "PT Sans", sans-serif; color: var(--ink); position: relative; }

  .card {
    position: absolute;
    top: 302px;
    width: 530px;
    height: 295px;
    box-shadow: 0 3px 10px rgba(0,0,0,0.18);
    overflow: hidden;
  }
  .card--front { left: 50px; background: #fff; }
  .card--back {
    left: 620px;
    background: radial-gradient(ellipse 55% 70% at 22% 50%, var(--green-glow) 0%, #c8e4ac 45%, var(--brand-green) 85%, var(--green-deep) 100%);
  }

  .wordmark {
    position: absolute;
    display: flex;
    align-items: center;
    gap: 8px;
    font-weight: 700;
    font-size: 15px;
    color: var(--brand-navy);
    letter-spacing: 0.2px;
    white-space: nowrap;
  }
  .wordmark__dot {
    width: 14px; height: 14px; border-radius: 50%;
    background: var(--brand-blue);
    flex: none;
  }
  .card--front .wordmark { left: 30px; top: 32px; }
  .card--back .wordmark { left: 45px; top: 138px; }

  .brand-artwork {
    position: absolute;
    left: 290px;
    top: 10px;
    width: 230px;
    height: 272px;
    border-radius: 50% 50% 8px 8px;
    background: linear-gradient(135deg, var(--brand-blue) 0%, var(--brand-navy) 30%, var(--brand-purple) 62%, var(--brand-green) 100%);
  }
  .brand-watermark {
    position: absolute;
    left: 286px;
    top: 37px;
    width: 234px;
    height: 258px;
    border-radius: 50% 50% 0 0;
    background: linear-gradient(160deg, rgba(255,255,255,0.45) 0%, rgba(255,255,255,0.22) 100%);
  }

  .holder { position: absolute; left: 30px; top: 104px; }
  .holder__name { font-size: 29px; font-weight: 400; line-height: 1.1; }
  .holder__role { font-size: 15px; line-height: 1.3; }

  .contact {
    position: absolute; left: 30px; top: 193px;
    list-style: none; font-size: 13px; line-height: 16px;
  }

  .colour-band {
    position: absolute; left: 0; right: 0; bottom: 0; height: 8px;
    display: flex;
  }
  .colour-band span { flex: 1; }
  .colour-band .blue { background: var(--brand-blue); }
  .colour-band .purple { background: var(--brand-purple); }
  .colour-band .green { background: var(--brand-green); }
</style>
</head>
<body>
  <section class="card card--front" aria-label="Business card front">
    <div class="wordmark"><span class="wordmark__dot"></span>Marlow Advisory Partners Pty Ltd</div>
    <div class="brand-artwork" role="img" aria-label="Large brand symbol in blue, purple and green"></div>
    <div class="holder">
      <p class="holder__name">Your Name</p>
      <p class="holder__role">Profession or Position</p>
    </div>
    <ul class="contact">
      <li>detail address : Street 12345</li>
      <li>Zip Code</li>
      <li>Phone :</li>
      <li>Fax :</li>
      <li>email :&nbsp; website :</li>
    </ul>
    <div class="colour-band"><span class="blue"></span><span class="purple"></span><span class="green"></span></div>
  </section>

  <section class="card card--back" aria-label="Business card back">
    <div class="brand-watermark" role="img" aria-label="Faded white brand symbol watermark"></div>
    <div class="wordmark"><span class="wordmark__dot"></span>Marlow Advisory Partners Pty Ltd</div>
  </section>
</body>
</html>
```